Packaging design and 3D mockups for new line of chocolates

Use the existing Tide Amber design colors and elements (including the chocolate swirl or another special effect, or anything you like), and design our new product line called "Quiet Marble" in a 3-pack designed for flowwrapping.

Then, create a 3D mockup of the same design on a white background.

You will find everything you need attached (the TideAmber design, an example of a 3-piece flowwrapped package, and a powerpoint with all information you'll need for this design). Contact me through the TideAmber site if you need any further details.

Color scheme: Elegant black with gold text foiling, gold background for the flavor (Hazelnut Truffle) and elegant gold outlines wherever you would like.

Target Market(s)

Health conscious women between 22-58

Industry/Entity Type

Health and wellness, gourmet indulgence

Requirements
Must have
• See instructions above

```html
<!DOCTYPE html>
<html lang="en">
<head>
<meta charset="utf-8">
<title>Quiet Marble – Hazelnut Truffle flow-wrap</title>
<link rel="stylesheet" href="https://fonts.googleapis.com/css2?family=Yellowtail&family=Montserrat:wght@600;700;800&display=swap">
<style>
  :root {
    --canvas: #f4f4f4;
    --wrap-black: #0b0b0b;
    --gold: #e6be3c;
    --gold-light: #f2d873;
    --gold-deep: #c99a1c;
    --cocoa: #3a1d0e;
    --cocoa-light: #7a4222;
    --white: #ffffff;
    --line: #8a8a8a;
  }
  * { margin: 0; padding: 0; box-sizing: border-box; }
  html, body { width: 1200px; height: 800px; overflow: hidden; background: var(--canvas); }
  .canvas { position: relative; width: 1200px; height: 800px; }

  .flow-pack { position: absolute; left: 80px; top: 240px; width: 1040px; height: 320px; }
  .flow-pack__shape { position: absolute; inset: 0; }

  .title-row {
    position: absolute; left: 100px; top: 84px;
    display: flex; align-items: center; gap: 28px;
  }
  .brand-name {
    font-family: "Yellowtail", cursive; font-weight: 400; font-size: 68px; line-height: 1;
    color: var(--gold); white-space: nowrap;
  }
  .flavour {
    font-family: "Montserrat", sans-serif; font-weight: 700;
    font-size: 21px; line-height: 1.25; color: var(--white); letter-spacing: .4px;
    white-space: nowrap;
  }
  .flavour::before {
    content: ""; display: block; width: 130px; height: 1px;
    background: var(--line); margin-bottom: 8px;
  }

  .claims {
    position: absolute; left: 140px; top: 226px;
    display: flex; align-items: center; list-style: none;
  }
  .claim {
    font-family: "Montserrat", sans-serif; font-weight: 800; font-size: 12px;
    color: var(--cocoa); background: var(--gold); letter-spacing: .3px;
    padding: 6px 20px; white-space: nowrap;
    clip-path: polygon(10px 0, calc(100% - 10px) 0, 100% 50%, calc(100% - 10px) 100%, 10px 100%, 0 50%);
  }
  .claims__link { width: 24px; height: 2px; background: var(--gold); }

  .swirl-art {
    position: absolute; left: 740px; top: 44px; width: 190px; height: 220px;
    border-radius: 50%;
    background: radial-gradient(circle at 50% 50%, var(--cocoa) 0 30%, var(--cocoa-light) 45%, rgba(58,29,14,.55) 62%, rgba(58,29,14,0) 72%);
  }

  .origin-badge {
    position: absolute; left: 905px; top: 26px; width: 50px; height: 50px;
    border-radius: 50%; background: var(--wrap-black);
    border: 3px solid var(--gold-deep);
  }

  .net-weight {
    position: absolute; left: 800px; top: 262px;
    font-family: "Montserrat", sans-serif; font-weight: 600; font-size: 15px;
    color: var(--gold-light); background: #1c1a14; padding: 4px 12px; white-space: nowrap;
  }
</style>
</head>
<body>
<main class="canvas">
  <section class="flow-pack" aria-label="Quiet Marble hazelnut truffle flow-wrap label">
    <svg class="flow-pack__shape" viewBox="0 0 1040 320" width="1040" height="320" aria-hidden="true">
      <defs>
        <linearGradient id="wrap-fill" x1="0" y1="0" x2="1" y2="0">
          <stop offset="0" stop-color="#0b0b0b"/>
          <stop offset="0.55" stop-color="#0b0b0b"/>
          <stop offset="0.74" stop-color="#6b5515"/>
          <stop offset="0.87" stop-color="#e6be3c"/>
          <stop offset="1" stop-color="#f2d873"/>
        </linearGradient>
      </defs>
      <polygon fill="url(#wrap-fill)" points="16,10 1024,10 1040,22.5 1024,35 1040,47.5 1024,60 1040,72.5 1024,85 1040,97.5 1024,110 1040,122.5 1024,135 1040,147.5 1024,160 1040,172.5 1024,185 1040,197.5 1024,210 1040,222.5 1024,235 1040,247.5 1024,260 1040,272.5 1024,285 1040,297.5 1024,310 16,310 0,297.5 16,285 0,272.5 16,260 0,247.5 16,235 0,222.5 16,210 0,197.5 16,185 0,172.5 16,160 0,147.5 16,135 0,122.5 16,110 0,97.5 16,85 0,72.5 16,60 0,47.5 16,35 0,22.5"/>
      <line x1="72" y1="10" x2="72" y2="310" stroke="#2a2a2a" stroke-width="2"/>
      <line x1="968" y1="10" x2="968" y2="310" stroke="#c99a1c" stroke-width="2"/>
    </svg>

    <div class="swirl-art" role="img" aria-label="Illustration of a hazelnut truffle inside a swirl of melted chocolate with hazelnut pieces"></div>

    <div class="title-row">
      <h1 class="brand-name">Quiet Marble</h1>
      <p class="flavour">HAZELNUT TRUFFLE<br>TRUFFE NOISETTE</p>
    </div>

    <ul class="claims">
      <li class="claim">PLANT-BASED</li>
      <li class="claims__link" aria-hidden="true"></li>
      <li class="claim">SMOOTH</li>
      <li class="claims__link" aria-hidden="true"></li>
      <li class="claim">VELVETY CHOCOLATES</li>
    </ul>

    <div class="origin-badge" aria-hidden="true"></div>
    <p class="net-weight">30g (3 pieces)</p>
  </section>
</main>
</body>
</html>
```